Plumbing website that stands out

Seo optimized, mobile friendly, easily editable word press Plumbing website with google reviews widget. And widget of revolving photos of completed work. Contact page and services page, about page. Will provide, “About” content. And photos Need all other content written.
Services include:
Water heater replacement
Tankless water heater installation
Kitchen and bath remodel
Drain cleaning and clog removal
Leak repair
Faucet repair and replacement

I will be adding services and photos of recent completed projects as time goes on.

```html
<!DOCTYPE html>
<html lang="en">
<head>
<meta charset="utf-8">
<title>Clearline Plumbing</title>
<link href="https://fonts.googleapis.com/css2?family=Cinzel:wght@400;600&family=Arimo:wght@400;700&display=swap" rel="stylesheet">
<style>
:root{
  --navy:#2a5597;
  --navy-deep:#1f4a8a;
  --teal:#5bb8cf;
  --teal-soft:#8fd0e0;
  --ink:#333;
  --muted:#555;
  --white:#fff;
  --star:#f5b400;
  --accent:#e0632a;
}
*{margin:0;padding:0;box-sizing:border-box}
html,body{width:1200px;height:5208px;overflow:hidden}
body{position:relative;background:var(--white);font-family:"Arimo",Arial,sans-serif;color:var(--ink)}
.abs{position:absolute}
h1,h2{font-family:"Cinzel",Georgia,serif;font-weight:400;letter-spacing:1px}
.btn{position:absolute;display:flex;align-items:center;justify-content:center;border-radius:24px;font-family:"Cinzel",Georgia,serif;font-size:17px;letter-spacing:1px;color:var(--white)}
.btn-solid{background:linear-gradient(90deg,var(--navy),var(--teal))}
.btn-line{border:2px solid var(--white)}
/* header */
.call{left:150px;top:18px;display:flex;gap:12px;align-items:center}
.call-icon{width:30px;height:30px;border-radius:50%;background:var(--teal);display:flex;align-items:center;justify-content:center}
.call small{display:block;font-family:"Cinzel",serif;color:var(--navy);font-size:15px}
.call span{font-size:14px;color:var(--muted)}
.brand{left:450px;top:14px;width:300px;text-align:center}
.brand-mark{width:44px;height:44px;background:var(--navy);margin:0 auto 6px}
.brand-name{font-family:"Cinzel",serif;font-size:24px;letter-spacing:4px;color:var(--navy)}
.brand-sub{font-family:"Cinzel",serif;font-size:9px;letter-spacing:6px;color:var(--teal)}
.nav{top:82px;font-family:"Cinzel",serif;font-size:13px;color:var(--muted);display:flex;gap:32px}
.nav .on{color:var(--teal)}
/* hero */
.hero{left:0;top:125px;width:1200px;height:665px;background:linear-gradient(90deg,#2a5597 0%,#3a6aa6 45%,#7d8ea5 75%,#5f6f86 100%)}
.hero h1{position:absolute;left:150px;top:155px;font-size:48px;line-height:54px;color:var(--white)}
.hero p{position:absolute;left:150px;top:285px;width:520px;font-size:13px;line-height:18px;color:var(--white)}
.section-head{position:absolute;left:0;width:1200px;text-align:center}
.section-head h2{font-size:46px;color:#4a4a4a}
.section-head h2 em{font-style:normal;color:var(--teal)}
.section-head p{width:780px;margin:18px auto 0;font-size:13px;line-height:19px}
.band{position:absolute;left:0;width:1200px}
.light h2,.light p{color:var(--white)}
/* about */
.about-art{left:175px;top:808px;width:415px;height:422px;background:linear-gradient(135deg,var(--navy) 55%,var(--teal) 100%)}
.about-text{left:645px;top:840px;width:410px}
.about-text h2{font-size:48px;color:#4a4a4a}
.about-text h2 em{font-style:normal;color:var(--teal)}
.about-text p{margin-top:22px;font-size:12.5px;line-height:17px}
/* services */
.svc{position:absolute;color:var(--white);width:300px}
.svc h3{font-size:14px;font-weight:700;margin-bottom:6px}
.svc p{font-size:11.5px;line-height:15px}
.svc.l{text-align:center}
.node{position:absolute;width:60px;height:60px;border-radius:50%;background:var(--teal);border:3px solid var(--white);display:flex;align-items:center;justify-content:center}
.proj{position:absolute}
/* features */
.feat{position:absolute;top:3355px;width:290px;height:175px;border:2px solid rgba(255,255,255,.8);overflow:hidden;color:var(--white)}
.feat h3{position:absolute;left:18px;top:38px;font-size:14px;font-weight:700}
.feat p{position:absolute;left:18px;top:66px;width:150px;font-size:11.5px;line-height:14px}
.feat .tab{position:absolute;right:0;top:0;width:110px;height:175px;background:var(--teal);clip-path:polygon(60% 0,100% 0,100% 100%,60% 100%,0 50%)}
.feat .ic{position:absolute;right:18px;top:60px}
/* reviews */
.review{position:absolute;top:4050px;width:288px;height:258px;border:2px solid #ddd;text-align:center;background:var(--white)}
.avatar{position:absolute;top:3997px;width:122px;height:122px;border-radius:50%;border:4px solid var(--navy);background:linear-gradient(135deg,#d8b9a4,#8d7062)}
.stars{margin-top:88px;display:flex;justify-content:center;align-items:center;gap:6px;font-size:14px}
.stars .g{width:22px;height:22px;border-radius:50%;background:#d6d6d6}
.stars b{color:var(--star);font-size:22px;letter-spacing:1px}
.review q{display:block;margin:14px auto 0;width:240px;font-style:italic;font-size:13px;line-height:17px;quotes:"\201C" "\201D"}
.review .who{margin-top:10px;font-family:"Cinzel",serif;color:var(--accent);font-size:14px}
.arrow{position:absolute;top:4185px;width:30px;height:30px;border-radius:50%;background:#9a9a9a;display:flex;align-items:center;justify-content:center}
/* contact */
.touch{left:187px;top:4425px;width:826px;height:410px;border-radius:40px 0 40px 0;background:linear-gradient(135deg,#1699b8,#4cc0dd)}
.touch h2{position:absolute;top:60px;width:100%;text-align:center;font-size:48px;color:var(--white)}
.field{position:absolute;border:1.5px solid rgba(255,255,255,.85);color:var(--white);font-size:11px;padding:8px 10px}
.foot-nav{left:0;top:5020px;width:1200px;display:flex;justify-content:center;gap:34px;font-family:"Cinzel",serif;font-size:13px;color:var(--white)}
.foot-info{top:5062px;display:flex;align-items:center;gap:10px;color:var(--white);font-size:12px}
.dot-ic{width:26px;height:26px;border-radius:50%;background:var(--teal);display:flex;align-items:center;justify-content:center}
.social{position:absolute;top:5160px;width:34px;height:34px;border-radius:50%;background:var(--white)}
</style>
</head>
<body>

<!-- header -->
<div class="abs call">
  <div class="call-icon"><svg width="16" height="16" viewBox="0 0 24 24"><path fill="#fff" d="M6.6 10.8a15 15 0 0 0 6.6 6.6l2.2-2.2c.3-.3.7-.4 1-.2 1.1.4 2.3.6 3.6.6.6 0 1 .4 1 1V20c0 .6-.4 1-1 1A17 17 0 0 1 3 4c0-.6.4-1 1-1h3.5c.6 0 1 .4 1 1 0 1.3.2 2.5.6 3.6.1.3 0 .7-.2 1z"/></svg></div>
  <div><small>Call Us</small><span>555 014 2290</span></div>
</div>
<div class="abs brand">
  <div class="brand-mark"></div>
  <div class="brand-name">CLEARLINE</div>
  <div class="brand-sub">PLUMBING</div>
</div>
<div class="abs nav" style="left:148px"><span class="on">HOME</span><span>ABOUT US</span><span>SERVICES</span></div>
<div class="abs nav" style="left:793px"><span>REVIEWS</span><span>GALLERY</span><span>CONTACT</span></div>
<div class="btn btn-solid" style="left:876px;top:16px;width:175px;height:46px">GET A QUOTE</div>

<!-- hero -->
<section class="abs hero" role="img" aria-label="Plumber fixing pipes with a wrench, blue overlay">
  <h1>COMPLETE PLUMBING<br>SOLUTIONS</h1>
  <p>Lorem ipsum dolor sit amet, consectetur adipiscing elit, sed do eiusmod tempor incididunt ut labore et dolore magna aliqua. Quis ipsum suspendisse ultrices gravida.</p>
  <div class="btn btn-line" style="left:150px;top:350px;width:188px;height:46px">GET IN TOUCH</div>
</section>
<svg class="abs" style="left:0;top:620px" width="1200" height="180" viewBox="0 0 1200 180">
  <path d="M0 150 C200 60 380 60 560 95 C760 135 950 120 1200 40 L1200 180 L0 180Z" fill="#fff"/>
  <path d="M0 165 C200 70 380 60 560 95 C760 135 950 120 1200 40 L1200 60 C960 150 760 160 560 115 C380 80 200 90 0 180Z" fill="#2a5597"/>
  <path d="M420 80 C600 60 760 150 1200 110 L1200 128 C760 170 600 90 420 80Z" fill="#5bb8cf"/>
</svg>

<!-- about -->
<div class="abs about-art" role="img" aria-label="Brand illustration of a plumber figure with flowing water"></div>
<div class="abs about-text">
  <h2>ABOUT <em>US</em></h2>
  <p>Lorem ipsum dolor sit amet, consectetur adipiscing elit, sed do eiusmod tempor incididunt ut labore et dolore magna aliqua. Ut enim ad minim veniam, quis nostrud exercitation ullamco laboris nisi ut aliquip ex ea commodo consequat. Duis aute irure dolor in reprehenderit in voluptate velit esse cillum dolore eu fugiat nulla pariatur. Excepteur sint occaecat cupidatat non proident, sunt in culpa qui officia deserunt mollit anim id est laborum. Sed ut perspiciatis unde omnis iste natus error sit voluptatem accusantium doloremque laudantium, totam rem aperiam, eaque ipsa quae ab illo inventore veritatis et quasi architecto beatae vitae dicta sunt explicabo.</p>
</div>
<div class="btn btn-solid" style="left:645px;top:1128px;width:162px;height:42px">READ MORE</div>

<!-- services -->
<section class="band light" style="top:1310px;height:790px">
  <div class="abs" style="left:0;top:70px;width:1200px;height:680px;background:linear-gradient(180deg,#2a5597,#2d5fa0)" role="img" aria-label="Plumbing van and workers, blue tinted"></div>
  <svg class="abs" style="left:0;top:0" width="1200" height="130" viewBox="0 0 1200 130">
    <path d="M0 0 H1200 V55 C950 120 800 70 600 60 C380 50 200 120 0 75Z" fill="#fff"/>
    <path d="M200 95 C420 30 620 60 800 80 C960 95 1080 60 1200 5 V40 C1080 90 960 115 800 100 C620 85 420 55 200 95Z" fill="#5bb8cf"/>
  </svg>
  <div class="section-head" style="top:160px">
    <h2>OUR SERVICES</h2>
    <p>Lorem ipsum dolor sit amet, consectetur adipiscing elit, sed do eiusmod tempor incididunt ut labore et dolore magna aliqua. Ut enim ad minim veniam, quis nostrud exercitation ullamco laboris nisi ut aliquip ex ea commodo consequat.</p>
  </div>
  <svg class="abs" style="left:370px;top:365px" width="460" height="420"><circle cx="230" cy="230" r="215" fill="none" stroke="#fff" stroke-width="2"/></svg>
  <div class="abs" style="left:435px;top:395px;width:330px;height:360px;border-radius:50% 50% 0 0;background:linear-gradient(180deg,#3c6aa9,#1e3c6e)" role="img" aria-label="Smiling plumber holding a wrench"></div>
  <div class="svc l" style="left:105px;top:345px"><h3>TANKLESS WATER HEATER INSTALLATION</h3><p>Lorem ipsum dolor sit amet, consectetur adipiscing elit, sed do eiusmod tempor incididunt aliqua.</p></div>
  <div class="svc l" style="left:105px;top:437px"><h3>KITCHEN AND BATH REMODEL</h3><p>Lorem ipsum dolor sit amet, consecteturelit, sed do eiusmod tempor incididunt aliqua.</p></div>
  <div class="svc l" style="left:75px;top:540px"><h3>WATER HEATER REPLACEMENT</h3><p>Lorem ipsum dolor sit amet, consecteturelit, sed do eiusmod tempor incididunt aliqua.</p></div>
  <div class="svc" style="left:745px;top:345px"><h3>DRAIN CLEANING AND CLOG REMOVAL</h3><p>Lorem ipsum dolor sit amet, consectetur adipiscing elit, sed do eiusmod tempor incididunt aliqua.</p></div>
  <div class="svc" style="left:828px;top:437px"><h3>LEAK REPAIR</h3><p>Lorem ipsum dolor sit amet, consecteturelit, sed do eiusmod tempor incididunt aliqua.</p></div>
  <div class="svc" style="left:863px;top:540px"><h3>FAUCET REPAIR &amp; REPLACEMENT</h3><p>Lorem ipsum dolor sit amet, consecteturelit, sed do eiusmod tempor incididunt aliqua.</p></div>
  <div class="node" style="left:458px;top:355px"><svg width="24" height="24"><path d="M12 3 C16 9 18 12 18 15 a6 6 0 0 1-12 0 c0-3 2-6 6-12z" fill="#fff"/></svg></div>
  <div class="node" style="left:375px;top:430px"><svg width="24" height="24"><rect x="4" y="8" width="16" height="12" fill="none" stroke="#fff" stroke-width="2"/></svg></div>
  <div class="node" style="left:345px;top:545px"><svg width="24" height="24"><rect x="7" y="3" width="10" height="18" rx="3" fill="none" stroke="#fff" stroke-width="2"/></svg></div>
  <div class="node" style="left:670px;top:355px"><svg width="24" height="24"><path d="M4 6 H20 L14 14 V20 H10 V14Z" fill="none" stroke="#fff" stroke-width="2"/></svg></div>
  <div class="node" style="left:752px;top:440px"><svg width="24" height="24"><path d="M12 3 C16 9 18 12 18 15 a6 6 0 0 1-12 0 c0-3 2-6 6-12z" fill="#fff"/></svg></div>
  <div class="node" style="left:782px;top:545px"><svg width="24" height="24"><path d="M6 20 V10 a6 6 0 0 1 12 0 V13" fill="none" stroke="#fff" stroke-width="2.5"/></svg></div>
  <svg class="abs" style="left:0;top:700px" width="1200" height="95" viewBox="0 0 1200 95">
    <path d="M0 40 C250 10 420 70 650 60 C850 52 1000 20 1200 0 V95 H0Z" fill="#fff"/>
    <path d="M0 28 C250 0 420 60 650 50 C850 42 1000 10 1200 -5 V10 C1000 30 850 62 650 72 C420 82 250 30 0 58Z" fill="#5bb8cf"/>
  </svg>
</section>

<!-- projects -->
<div class="section-head" style="top:2170px">
  <h2>LATEST <em>PROJECTS</em></h2>
  <p>Lorem ipsum dolor sit amet, consectetur adipiscing elit, sed do eiusmod tempor incididunt ut labore et dolore magna aliqua. Ut enim ad minim veniam, quis nostrud exercitation ullamco laboris nisi ut aliquip ex ea commodo consequat.</p>
</div>
<div class="proj" style="left:150px;top:2325px;width:442px;height:270px;background:linear-gradient(135deg,#9aa5b2,#4a5a70)" role="img" aria-label="Plumber fitting a boiler pipe"></div>
<div class="proj" style="left:610px;top:2325px;width:210px;height:270px;background:linear-gradient(135deg,#d7dde3,#8a96a3)" role="img" aria-label="Chrome faucet being repaired"></div>
<div class="proj" style="left:838px;top:2325px;width:210px;height:270px;background:linear-gradient(135deg,#c9c2b5,#6f7d8e)" role="img" aria-label="Worker in helmet fixing water pipes"></div>
<div class="proj" style="left:150px;top:2615px;width:215px;height:270px;background:linear-gradient(135deg,#8c8f92,#3e5f8a)" role="img" aria-label="Boiler room pipework with expansion tank"></div>
<div class="proj" style="left:380px;top:2615px;width:212px;height:270px;background:linear-gradient(135deg,#e3e3e3,#5f6f86)" role="img" aria-label="Plumber servicing a water heater"></div>
<div class="proj" style="left:610px;top:2615px;width:442px;height:270px;background:linear-gradient(135deg,#6e6e6e,#cfd8de)" role="img" aria-label="Hands tightening a sink drain pipe with pliers"></div>
<div class="btn btn-solid" style="left:530px;top:2930px;width:140px;height:42px">VIEW ALL</div>

<!-- features -->
<section class="band light" style="top:3015px;height:780px;background:linear-gradient(180deg,#2a5597,#3b80b3)">
  <svg class="abs" style="left:0;top:0" width="1200" height="130" viewBox="0 0 1200 130">
    <path d="M0 0 H1200 V45 C950 100 800 40 600 50 C380 60 200 110 0 90Z" fill="#fff"/>
    <path d="M220 100 C420 40 620 55 800 60 C960 65 1080 40 1200 15 V35 C1080 70 960 85 800 80 C620 75 420 60 220 100Z" fill="#5bb8cf"/>
  </svg>
  <div class="section-head" style="top:185px">
    <h2>OUR FEATURES</h2>
    <p>Lorem ipsum dolor sit amet, consectetur adipiscing elit, sed do eiusmod tempor incididunt ut labore et dolore magna aliqua. Ut enim ad minim veniam, quis nostrud exercitation ullamco laboris nisi ut aliquip ex ea commodo consequat.</p>
  </div>
  <svg class="abs" style="left:0;top:690px" width="1200" height="90" viewBox="0 0 1200 90">
    <path d="M0 50 C250 20 420 80 650 60 C850 45 1000 15 1200 0 V90 H0Z" fill="#fff"/>
    <path d="M0 38 C250 8 420 68 650 48 C850 33 1000 5 1200 -8 V8 C1000 25 850 58 650 72 C420 90 250 35 0 65Z" fill="#5bb8cf"/>
  </svg>
</section>
<div class="feat" style="left:148px"><h3>PROFFESIONAL WORKER</h3><p>Lorem ipsum dolor sit amet, consectetur adipiscing elit, sed do eiusmod tempor incididunt ut labore et dolore magna aliqua.</p><div class="tab"></div>
  <svg class="ic" width="50" height="50"><circle cx="25" cy="12" r="7" fill="none" stroke="#2a5597" stroke-width="3"/><path d="M8 44 a17 17 0 0 1 34 0" fill="none" stroke="#2a5597" stroke-width="3"/></svg></div>
<div class="feat" style="left:457px"><h3>24/7 SERVICE</h3><p>Lorem ipsum dolor sit amet, consectetur adipiscing elit, sed do eiusmod tempor incididunt ut labore et dolore magna aliqua.</p><div class="tab"></div>
  <svg class="ic" width="50" height="50"><circle cx="25" cy="25" r="20" fill="none" stroke="#fff" stroke-width="3"/><text x="25" y="30" text-anchor="middle" fill="#fff" font-family="Arimo,sans-serif" font-size="13">24/7</text></svg></div>
<div class="feat" style="left:763px"><h3>AFFORDABLE PRICE</h3><p>Lorem ipsum dolor sit amet, consectetur adipiscing elit, sed do eiusmod tempor incididunt ut labore et dolore magna aliqua.</p><div class="tab"></div>
  <svg class="ic" width="50" height="50"><circle cx="28" cy="16" r="11" fill="none" stroke="#2a5597" stroke-width="3"/><text x="28" y="21" text-anchor="middle" fill="#2a5597" font-family="Arimo,sans-serif" font-size="13">$</text><path d="M4 40 H18 L30 36 H44" fill="none" stroke="#2a5597" stroke-width="3"/></svg></div>
<div class="btn btn-line" style="left:515px;top:3590px;width:170px;height:46px">CONTACT US</div>

<!-- reviews -->
<div class="section-head" style="top:3835px">
  <h2>CLIENT <em>REVIEWS</em></h2>
  <p>Lorem ipsum dolor sit amet, consectetur adipiscing elit, sed do eiusmod tempor incididunt ut labore et dolore magna aliqua. Ut enim ad minim veniam, quis nostrud exercitation ullamco laboris nisi ut aliquip ex ea commodo consequat.</p>
</div>
<div class="arrow" style="left:55px"><svg width="14" height="14"><path d="M12 7 H3 M7 2 L2 7 L7 12" fill="none" stroke="#fff" stroke-width="2"/></svg></div>
<div class="arrow" style="left:1115px"><svg width="14" height="14"><path d="M2 7 H11 M7 2 L12 7 L7 12" fill="none" stroke="#fff" stroke-width="2"/></svg></div>
<div class="review" style="left:143px"><div class="stars"><span class="g"></span><b>★★★★★</b>5 star review</div><q>Lorem ipsum dolor sit amet, consecter adipiscing elit, sed do eiusmod tempor incididunt ut labore et dolore magna aliqua.consequat loreum psium</q><div class="who">- DANA WHITFIELD</div></div>
<div class="review" style="left:459px"><div class="stars"><span class="g"></span><b>★★★★★</b>5 star review</div><q>Lorem ipsum dolor sit amet, consecter adipiscing elit, sed do eiusmod tempor incididunt ut labore et dolore magna aliqua.consequat loreum psium</q><div class="who">- MARCO ELLERY</div></div>
<div class="review" style="left:770px"><div class="stars"><span class="g"></span><b>★★★★★</b>5 star review</div><q>Lorem ipsum dolor sit amet, consecter adipiscing elit, sed do eiusmod tempor incididunt ut labore et dolore magna aliqua.consequat loreum psium</q><div class="who">- OWEN CASTELL</div></div>
<div class="avatar" style="left:225px" role="img" aria-label="Client photo"></div>
<div class="avatar" style="left:541px" role="img" aria-label="Client photo"></div>
<div class="avatar" style="left:853px" role="img" aria-label="Client photo"></div>

<!-- contact + footer -->
<div class="band" style="top:4580px;height:628px;background:linear-gradient(180deg,#2a5597,#2d5c9c)" role="img" aria-label="Plumbing work scene, blue tinted"></div>
<svg class="abs" style="left:0;top:4560px" width="1200" height="120" viewBox="0 0 1200 120">
  <path d="M0 60 C300 20 600 90 900 70 C1030 60 1120 40 1200 20 V0 H0Z" fill="#fff"/>
  <path d="M0 50 C300 10 600 80 900 60 C1030 50 1120 30 1200 10 V25 C1120 45 1030 70 900 80 C600 100 300 30 0 72Z" fill="#5bb8cf"/>
</svg>
<div class="abs touch">
  <h2>GET IN TOUCH</h2>
  <div class="field" style="left:45px;top:140px;width:353px;height:38px">Name</div>
  <div class="field" style="left:45px;top:198px;width:353px;height:38px">Email Address</div>
  <div class="field" style="left:45px;top:254px;width:353px;height:38px">Phone Number</div>
  <div class="field" style="left:425px;top:140px;width:355px;height:152px">Message</div>
  <div class="btn btn-line" style="left:348px;top:322px;width:126px;height:46px">SUBMIT</div>
</div>
<div class="abs brand" style="top:4900px">
  <div class="brand-mark" style="background:#fff"></div>
  <div class="brand-name" style="color:#fff">CLEARLINE</div>
  <div class="brand-sub" style="color:#fff">PLUMBING</div>
</div>
<div class="abs foot-nav"><span>HOME</span><span>ABOUT US</span><span>SERVICES</span><span>REVIEWS</span><span>GALLERY</span><span>CONTACT</span></div>
<div class="abs foot-info" style="left:276px"><span class="dot-ic"><svg width="12" height="14"><path d="M6 13 C2 8 1 6 1 5 a5 5 0 0 1 10 0 c0 1-1 3-5 8z" fill="#fff"/></svg></span><span>123 ipsum dolor sit<br>amet, consectetur</span></div>
<div class="abs foot-info" style="left:525px"><span class="dot-ic"><svg width="12" height="12" viewBox="0 0 24 24"><path fill="#fff" d="M6.6 10.8a15 15 0 0 0 6.6 6.6l2.2-2.2c.3-.3.7-.4 1-.2 1.1.4 2.3.6 3.6.6.6 0 1 .4 1 1V20c0 .6-.4 1-1 1A17 17 0 0 1 3 4c0-.6.4-1 1-1h3.5c.6 0 1 .4 1 1 0 1.3.2 2.5.6 3.6.1.3 0 .7-.2 1z"/></svg></span><span>555 014 2290</span></div>
<div class="abs foot-info" style="left:750px"><span class="dot-ic"><svg width="14" height="10"><rect x="1" y="1" width="12" height="8" fill="none" stroke="#fff"/><path d="M1 1 L7 6 L13 1" fill="none" stroke="#fff"/></svg></span><span>info@clearlineplumbing.com</span></div>
<div class="abs" style="left:150px;top:5168px;font-family:'Cinzel',serif;font-size:14px;color:#fff">© 2023 CLEARLINE PLUMBING</div>
<div class="social" style="left:922px" aria-label="Social link"></div>
<div class="social" style="left:968px" aria-label="Social link"></div>
<div class="social" style="left:1014px" aria-label="Social link"></div>

</body>
</html>
```